Elegant Tavaroa Rhum Label Design-

We are creating a Rum Distillery in the paradise island of Bora Bora which is a beautiful and exclusive honeymoon and tourist destination in the South Pacific. Our Rum label needs to reflect the beauty of Bora Bora and French Polynesia.
We would like to see designs that include the image of Mount Otemanu (* the mountain of Bora Bora) with an overwater bungalow in the image with the lagoon. We would like the label to have a turquoise color theme with either silver, white, or gold as the outline of the images. We are also open to some tropical colors as well that represent this paradise. The image needs to represent high quality class. The bottle will be sold mostly to tourist at a premium price.

On the label it needs to have Tavaroa Rhum as the main name-
Subheader- Light Rhum
Sub Sub header- Distilled and Bottled in Bora Bora
It needs to have 40% vol and 70cl on the label

Target Market(s)

American tourists in Bora Bora, French Polynesia

Industry/Entity Type

Rum Distillery

Colors
0094D4
00A9DD
6FCCEA
C7EBF8
E9F6FB
00AB8E
00BBA5
67D7C9
C6EFE9
E9F9F6

Requirements
Must have
• The mountain image of Otemanu and an overwater bungalow which is symbolic of Bora Bora.

```html
<!DOCTYPE html>
<html lang="en">
<head>
<meta charset="utf-8">
<title>Tavaroa Rhum – Light White Rum Label</title>
<link href="https://fonts.googleapis.com/css2?family=Cinzel:wght@600;700;900&family=Playfair+Display:wght@700&family=Great+Vibes&display=swap" rel="stylesheet">
<style>
  :root {
    --page: #ffffff;
    --label-cream: #f3f1e6;
    --label-cream-edge: #e9e6d6;
    --info-paper: #efe9cf;
    --ink: #232323;
    --ink-soft: #3a3a3a;
    --teal: #2a9aa0;
    --slate: #6a6d7c;
    --gold-light: #cfae66;
    --gold-dark: #8c6a2a;
    --rule: #b9b3a0;
    --flag-red: #d0262f;
    --sky: #c7ebf8;
    --sky-mid: #9fd8ee;
    --lagoon-pale: #c6efe9;
    --lagoon: #67d7c9;
  }
  * { box-sizing: border-box; margin: 0; padding: 0; }
  html, body {
    width: 1200px; height: 1200px; overflow: hidden;
    background: var(--page);
  }
  .canvas { position: relative; width: 1200px; height: 1200px; }
  .label {
    position: absolute; left: 280px; top: 30px;
    width: 640px; height: 1140px;
    background: linear-gradient(90deg, var(--label-cream-edge) 0%, var(--label-cream) 18%, var(--label-cream) 82%, var(--label-cream-edge) 100%);
    overflow: hidden;
  }
  .centered { position: absolute; left: 0; width: 100%; text-align: center; }
  .premium {
    top: 50px; font-family: "Great Vibes", cursive; font-size: 44px;
    color: var(--teal); transform: rotate(-3deg);
  }
  .diamond { position: absolute; left: 311px; top: 99px; width: 14px; height: 8px; }
  .est {
    top: 116px; font-family: "Cinzel", serif; font-weight: 700;
    font-size: 24px; letter-spacing: 1px; color: var(--ink);
  }
  .brand-name {
    top: 156px; font-family: "Playfair Display", serif; font-weight: 700;
    font-size: 108px; line-height: 1; letter-spacing: 2px; color: var(--ink);
  }
  .product {
    top: 272px; font-family: "Cinzel", serif; font-weight: 900;
    font-size: 78px; line-height: 1; letter-spacing: 3px; color: var(--teal);
  }
  .descriptor {
    top: 362px; font-family: "Cinzel", serif; font-weight: 700;
    font-size: 30px; letter-spacing: 1px; color: var(--slate);
  }
  .info-panel {
    position: absolute; left: 25px; top: 419px; width: 568px; height: 250px;
    background: var(--info-paper);
    background-image: repeating-linear-gradient(0deg, rgba(184,144,68,0.08) 0 1px, transparent 1px 7px);
  }
  .seal {
    position: absolute; left: 43px; top: 62px; width: 130px; height: 130px;
    border-radius: 50%; border: 2px dotted var(--gold-light);
    background: rgba(207,174,102,0.25);
  }
  .panel-divider {
    position: absolute; left: 203px; top: 30px; width: 1px; height: 190px;
    background: var(--rule);
  }
  .flag { position: absolute; left: 225px; top: 31px; width: 68px; height: 44px; }
  .origin {
    position: absolute; left: 305px; top: 38px;
    font-family: "Cinzel", serif; font-weight: 700; font-size: 12px;
    line-height: 1.25; color: var(--ink-soft);
  }
  .field {
    position: absolute; left: 225px; width: 305px;
    font-family: "Cinzel", serif; font-weight: 700; font-size: 17px; color: var(--ink);
  }
  .field.batch { top: 91px; }
  .field.bottle { top: 134px; }
  .field-rule { position: absolute; left: 225px; width: 305px; border-top: 1px dashed var(--rule); }
  .field-rule.one { top: 121px; }
  .field-rule.two { top: 164px; }
  .spec {
    position: absolute; left: 225px; top: 178px;
    font-family: "Cinzel", serif; font-weight: 700; font-size: 21px;
    line-height: 1.2; color: var(--ink);
  }
  .edition-band {
    position: absolute; left: 0; top: 700px; width: 100%; height: 74px;
    background: linear-gradient(90deg, var(--gold-dark), var(--gold-light) 30%, var(--gold-light) 70%, var(--gold-dark));
    display: flex; align-items: center; justify-content: center;
    font-family: "Great Vibes", cursive; font-size: 40px; color: var(--ink);
  }
  .scene-art {
    position: absolute; left: 0; top: 800px; width: 100%; height: 340px;
    background: linear-gradient(180deg,
      var(--label-cream) 0%,
      var(--sky) 28%,
      var(--sky-mid) 48%,
      var(--lagoon-pale) 66%,
      var(--lagoon) 84%,
      var(--label-cream) 100%);
  }
</style>
</head>
<body>
<main class="canvas">
  <section class="label">
    <div class="centered premium">Premium Rum</div>
    <svg class="diamond" viewBox="0 0 14 8" aria-hidden="true"><polygon points="0,4 7,0 14,4 7,8" fill="#b89044"/></svg>
    <div class="centered est">Est. 2025</div>
    <h1 class="centered brand-name">TAVAROA</h1>
    <div class="centered product">RUM</div>
    <div class="centered descriptor">A Light White Rum</div>

    <div class="info-panel">
      <div class="seal" aria-hidden="true"></div>
      <div class="panel-divider"></div>
      <svg class="flag" viewBox="0 0 68 44" aria-hidden="true">
        <rect width="68" height="11" fill="#d0262f"/>
        <rect y="11" width="68" height="22" fill="#ffffff"/>
        <rect y="33" width="68" height="11" fill="#d0262f"/>
      </svg>
      <div class="origin">Distilled &amp; Bottled in:<br>Bora Bora,<br>French Polynesia</div>
      <div class="field batch">Batch No.:</div>
      <div class="field-rule one"></div>
      <div class="field bottle">Bottle No.:</div>
      <div class="field-rule two"></div>
      <div class="spec">40% Alc Vol.<br>700ml</div>
    </div>

    <div class="edition-band">Small Batch &nbsp;•&nbsp; Limited Edition</div>

    <div class="scene-art" role="img" aria-label="Watercolour illustration of Mount Otemanu rising above overwater bungalows on a turquoise lagoon"></div>
  </section>
</main>
</body>
</html>
```